Local Electrical company need some kick ass business cards

In need of some in your face design business cards for a family owned electrical service company in Edmonton, Alberta Canada. We provide reliable and trustworthy electrical service for commercial and residential work in the Edmonton and area. We have been in business for 25 years.

Target Market(s)

Residential and commercial electrical

Industry/Entity Type

Business

Contact Information for Business Card

Your welcome to change and modify the Vantor Wiring logo. please include the lightbulb! Our Colours are black and green please stay with that.
Please include a name phone number and address on the card
phone number - 780-555-0138
#22, 418 Maple Ridge Rd, St.Albert, Alberta.
Two things that need to be on the card.
"your friendly neighborhood electrictrician"
Commercial & residential electrical repair and service

Colors
9bcb3c

Requirements
Must have
• Light bulb guy Attached
• "your friendly neighborhood electrictrician"
• Commercial & residential electrical repair and service
• phone number - 780-555-0138
• #22, 418 Maple Ridge Rd, St.Albert, Alberta.
• Our colours are black and green
Nice to have
• go wild i want something loud

```html
<!DOCTYPE html>
<html lang="en">
<head>
<meta charset="utf-8">
<title>Vantor Wiring — Business Cards</title>
<link rel="stylesheet" href="https://fonts.googleapis.com/css2?family=Open+Sans:wght@400;600;700;800&display=swap">
<style>
  :root {
    --green: #9bcb3c;
    --green-deep: #7fae22;
    --green-dark: #3d5a0c;
    --black: #0d0d0d;
    --paper: #f1f1ee;
    --ink: #111;
    --ink-muted: #666;
    --stage: #d9d9d6;
  }
  * { box-sizing: border-box; margin: 0; padding: 0; }
  html, body { width: 1200px; height: 900px; overflow: hidden; }
  body {
    background: var(--stage);
    font-family: "Open Sans", Arial, sans-serif;
    position: relative;
  }
  .card {
    position: absolute;
    overflow: hidden;
    box-shadow: 0 6px 18px rgba(0,0,0,.18);
  }

  /* Front: portrait card, content set along the long edge */
  .card-front {
    left: 90px; top: 135px;
    width: 360px; height: 630px;
    background: var(--paper);
  }
  .front-layout {
    position: absolute; left: 0; top: 0;
    width: 630px; height: 360px;
    transform-origin: top left;
    transform: translateX(360px) rotate(90deg);
  }
  .front-brand-panel {
    position: absolute; left: 0; top: 0; bottom: 0; width: 250px;
    background: var(--black);
    display: flex; align-items: center; justify-content: center;
  }
  .brand-name {
    color: var(--green);
    font-weight: 800;
    font-size: 32px;
    line-height: 1.05;
    text-align: center;
    margin-top: -60px;
  }
  .holder { position: absolute; left: 370px; top: 40px; }
  .holder-name { font-weight: 700; font-size: 24px; color: var(--ink); line-height: 1.1; }
  .holder-role { font-size: 13px; color: var(--ink-muted); }

  .contact-band {
    position: absolute; left: 212px; height: 40px;
    background: var(--green);
    display: flex; align-items: center;
    clip-path: polygon(0 0, 100% 0, calc(100% - 18px) 100%, 0 100%);
  }
  .band-icon {
    width: 44px; height: 100%;
    background: var(--green-deep);
    display: flex; align-items: center; justify-content: center;
    flex: none;
  }
  .band-text {
    padding-left: 12px; font-size: 14px; color: var(--ink); white-space: nowrap;
  }
  .band-phone   { top: 140px; width: 260px; }
  .band-address { top: 205px; width: 400px; }
  .band-email   { top: 270px; width: 280px; }

  /* Back */
  .card-back {
    left: 510px; top: 268px;
    width: 620px; height: 354px;
    background: var(--green);
  }
  .back-oval { position: absolute; inset: 0; }
  .back-content { position: absolute; left: 110px; top: 50px; width: 440px; }
  .mascot {
    width: 52px; height: 60px; border-radius: 10px;
    background: linear-gradient(160deg, #e8eef0, var(--green));
  }
  .tagline-main { color: var(--green); font-size: 22px; line-height: 1.2; margin-top: 14px; }
  .tagline-sub  { color: var(--green); font-size: 13px; margin-top: 8px; }
</style>
</head>
<body>

<section class="card card-front">
  <div class="front-layout">
    <div class="front-brand-panel">
      <div class="brand-name">Vantor<br>Wiring</div>
    </div>

    <div class="holder">
      <div class="holder-name">Name</div>
      <div class="holder-role">Founder</div>
    </div>

    <div class="contact-band band-phone">
      <span class="band-icon">
        <svg width="20" height="20" viewBox="0 0 24 24" aria-hidden="true"><path fill="#111" d="M6.6 10.8a15.2 15.2 0 0 0 6.6 6.6l2.2-2.2c.3-.3.7-.4 1-.2 1.1.4 2.3.6 3.6.6.6 0 1 .4 1 1V20c0 .6-.4 1-1 1A17 17 0 0 1 3 4c0-.6.4-1 1-1h3.5c.6 0 1 .4 1 1 0 1.3.2 2.5.6 3.6.1.3 0 .7-.2 1z"/></svg>
      </span>
      <span class="band-text">780-555-0138</span>
    </div>

    <div class="contact-band band-address">
      <span class="band-icon">
        <svg width="20" height="20" viewBox="0 0 24 24" aria-hidden="true"><path fill="#111" d="M12 3 2 12h3v8h5v-6h4v6h5v-8h3z"/></svg>
      </span>
      <span class="band-text">#22, 418 Maple Ridge Rd, St.Albert, Alberta.</span>
    </div>

    <div class="contact-band band-email">
      <span class="band-icon">
        <svg width="20" height="20" viewBox="0 0 24 24" aria-hidden="true" fill="none" stroke="#111" stroke-width="1.8"><circle cx="12" cy="12" r="9"/><ellipse cx="12" cy="12" rx="4" ry="9"/><path d="M3 12h18M5 7h14M5 17h14"/></svg>
      </span>
      <span class="band-text">hello@vantorwiring.ca</span>
    </div>
  </div>
</section>

<section class="card card-back">
  <svg class="back-oval" width="620" height="354" viewBox="0 0 620 354" aria-hidden="true">
    <defs>
      <radialGradient id="ovalFill" cx="45%" cy="40%" r="60%">
        <stop offset="0" stop-color="#1f1f1f"/>
        <stop offset="1" stop-color="#050505"/>
      </radialGradient>
    </defs>
    <ellipse cx="335" cy="172" rx="300" ry="205" fill="#3d5a0c"/>
    <ellipse cx="335" cy="172" rx="289" ry="196" fill="url(#ovalFill)"/>
  </svg>
  <div class="back-content">
    <div class="mascot" role="img" aria-label="Light bulb mascot character wearing a green cap"></div>
    <p class="tagline-main">Commercial &amp; residential electrical<br>repair and service</p>
    <p class="tagline-sub">Your friendly neighborhood electrictrician</p>
  </div>
</section>

</body>
</html>
```